Animal Eye Clinic needs a Business card

We are a new veterinary ophthalmology practice (Tessaly Animal Eye Care) and we need a business card designed. We only see animal eyes - we are not a regular veterinary clinic. We already have a logo. We are looking for a professional, good looking business card to hand out to our clients. We are looking for something simple but professional and contemporary. Our logo is likely the only picture/graphic that needs to be on the card.
Updates

Contact Information for Business Card

Marisol Dunkley, BSc, DVM, MSc, DipACVO
Veterinary Ophthalmologist

Phone: 250.418.3097
Email: tessalyanimaleyecare@mailbrook.net
Website: tessalyanimaleyecare.net
Address: 1840 Pellworth Rd
Kelowna, BC, V4T 8M3

Colors

Designer to choose colors to be used in the design.

Requirements
Must have
• Our logo (attached)

```html
<!DOCTYPE html>
<html lang="en">
<head>
<meta charset="utf-8">
<title>Tessaly Animal Eye Care – Business Card</title>
<link href="https://fonts.googleapis.com/css2?family=Roboto:ital,wght@0,400;0,700;1,400&display=swap" rel="stylesheet">
<style>
  :root {
    --teal: #0f97a8;
    --ink: #6a6a6a;
    --rule: #8c8c8c;
    --paper: #ffffff;
    --backdrop: #e6e7e8;
  }
  * { box-sizing: border-box; margin: 0; padding: 0; }
  html, body {
    width: 1200px; height: 1200px; overflow: hidden;
    background: var(--backdrop);
    font-family: "Roboto", Arial, sans-serif;
  }
  .sheet {
    width: 1200px; height: 1200px;
    display: flex; flex-direction: column; align-items: center; justify-content: center;
    gap: 40px;
  }
  .card {
    position: relative;
    width: 880px; height: 503px;
    background: var(--paper);
    border-radius: 26px;
    box-shadow: 0 6px 22px rgba(0,0,0,.18);
    overflow: hidden;
  }
  /* front */
  .card--front .brand {
    position: absolute; left: 0; right: 0; top: 190px;
    display: flex; align-items: center; justify-content: center; gap: 22px;
  }
  .brand-dot {
    width: 70px; height: 70px; border-radius: 50%;
    background: var(--teal);
  }
  .brand-name {
    font-weight: 700; color: var(--teal);
    font-size: 44px; letter-spacing: 0.5px;
  }
  .card--front .site {
    position: absolute; left: 0; right: 0; bottom: 60px;
    text-align: center; color: var(--ink);
    font-style: italic; font-size: 22px;
  }
  /* back */
  .card--back .mark {
    position: absolute; left: 60px; top: 150px; width: 270px;
    display: flex; flex-direction: column; align-items: center; gap: 18px;
  }
  .card--back .brand-dot { width: 110px; height: 110px; }
  .card--back .brand-name { font-size: 26px; text-align: center; line-height: 1.2; }
  .divider {
    position: absolute; left: 360px; top: 95px;
    width: 1px; height: 300px; background: var(--rule);
  }
  .contact {
    position: absolute; left: 395px; top: 105px; right: 30px;
    color: var(--ink); font-size: 22px; line-height: 1.3;
  }
  .person { color: var(--teal); font-weight: 700; font-size: 25px; }
  .role { margin-bottom: 10px; }
  .company { color: var(--teal); }
  .address { margin-bottom: 10px; }
  .line { display: flex; align-items: center; gap: 10px; }
  .line svg { width: 20px; height: 20px; flex: none; }
</style>
</head>
<body>
<main class="sheet">
  <section class="card card--front">
    <div class="brand">
      <span class="brand-dot"></span>
      <span class="brand-name">Tessaly Animal Eye Care</span>
    </div>
    <p class="site">tessalyanimaleyecare.net</p>
  </section>

  <section class="card card--back">
    <div class="mark">
      <span class="brand-dot"></span>
      <span class="brand-name">Tessaly Animal<br>Eye Care</span>
    </div>
    <div class="divider"></div>
    <div class="contact">
      <p class="person">Marisol Dunkley, BSc, DVM, MSc, DipACVO</p>
      <p class="role">Veterinary Ophthalmologist</p>
      <p class="company">Tessaly Animal Eye Care</p>
      <p class="address">1840 Pellworth Rd<br>Kelowna, BC, V4T 8M3</p>
      <p class="line">
        <svg viewBox="0 0 24 24" aria-hidden="true"><path fill="#0f97a8" d="M6.6 10.8a15 15 0 0 0 6.6 6.6l2.2-2.2c.3-.3.7-.4 1-.2 1.1.4 2.3.6 3.6.6.6 0 1 .4 1 1V20c0 .6-.4 1-1 1A17 17 0 0 1 3 4c0-.6.4-1 1-1h3.5c.6 0 1 .4 1 1 0 1.3.2 2.5.6 3.6.1.3 0 .7-.2 1z"/></svg>
        250.418.3097
      </p>
      <p class="line">
        <svg viewBox="0 0 24 24" aria-hidden="true"><rect x="2" y="5" width="20" height="14" fill="none" stroke="#0f97a8" stroke-width="2"/><path d="M2 5l10 8 10-8" fill="none" stroke="#0f97a8" stroke-width="2"/></svg>
        tessalyanimaleyecare@mailbrook.net
      </p>
      <p class="line">
        <svg viewBox="0 0 24 24" aria-hidden="true"><g fill="none" stroke="#0f97a8" stroke-width="1.6"><circle cx="12" cy="12" r="10"/><ellipse cx="12" cy="12" rx="4.5" ry="10"/><path d="M2 12h20M4 7h16M4 17h16"/></g></svg>
        tessalyanimaleyecare.net
      </p>
    </div>
  </section>
</main>
</body>
</html>
```